Business Card Design Project

I need a cool business card design for the company that will build residential houses.
The card should include:
1) Name: Boris Kalinov
2) Cell: 587.204.XXXX
3) Email: bor.kalinov@qwvend.example
4) Position: General Manager
5) Residential Home Building
6) Company logo that I have uploaded

Industry/Entity Type

Residential

```html
<!DOCTYPE html>
<html lang="en">
<head>
<meta charset="utf-8">
<title>Halvera Developments – Business Card</title>
<link rel="stylesheet" href="https://fonts.googleapis.com/css2?family=Open+Sans:wght@400;600;700&display=swap">
<style>
  :root {
    --stage: #ecebe8;
    --card-white: #ffffff;
    --brand-blue: #1e4a9b;
    --brand-green: #4fb04a;
    --green-light: #6cc15a;
    --green-dark: #45a93f;
    --text-white: #ffffff;
    --shadow: rgba(0, 0, 0, 0.22);
  }
  * { margin: 0; padding: 0; box-sizing: border-box; }
  html, body {
    width: 1200px;
    height: 836px;
    overflow: hidden;
    background: var(--stage);
    font-family: "Open Sans", Arial, sans-serif;
  }
  .stage {
    position: relative;
    width: 1200px;
    height: 836px;
  }
  .card {
    position: absolute;
    left: 340px;
    width: 520px;
    height: 300px;
    border-radius: 22px;
    overflow: hidden;
    box-shadow: 0 10px 26px var(--shadow);
  }

  /* Front */
  .card-front { top: 70px; background: var(--card-white); }
  .front-logo {
    position: absolute;
    left: 56px;
    top: 72px;
    display: flex;
    align-items: center;
    gap: 10px;
  }
  .logo-dot {
    width: 14px;
    height: 14px;
    border-radius: 50%;
    background: var(--brand-green);
  }
  .logo-name {
    font-weight: 700;
    font-size: 30px;
    letter-spacing: 0.5px;
    color: var(--brand-blue);
    line-height: 1;
  }
  .logo-sub {
    position: absolute;
    left: 80px;
    top: 108px;
    font-size: 11px;
    font-weight: 700;
    letter-spacing: 3px;
    color: var(--brand-blue);
  }
  .tagline {
    position: absolute;
    left: 56px;
    top: 130px;
    font-size: 15px;
    color: var(--brand-blue);
  }
  .person {
    position: absolute;
    right: 60px;
    top: 54px;
    text-align: left;
    font-size: 13px;
    line-height: 1.35;
  }
  .person-name { color: var(--brand-blue); }
  .person-role { color: var(--brand-green); }
  .front-rule {
    position: absolute;
    left: 0;
    right: 0;
    top: 170px;
    height: 4px;
    background: var(--brand-green);
  }
  .front-band {
    position: absolute;
    left: 0;
    right: 0;
    top: 178px;
    bottom: 0;
    background: var(--brand-blue);
  }
  .contact {
    position: absolute;
    left: 56px;
    bottom: 40px;
    color: var(--text-white);
    font-size: 13px;
    line-height: 1.45;
  }

  /* Back */
  .card-back {
    top: 470px;
    background: radial-gradient(ellipse at 55% 40%, var(--green-light) 0%, var(--green-dark) 75%);
  }
  .back-logo {
    position: absolute;
    left: 0;
    right: 0;
    top: 108px;
    display: flex;
    flex-direction: column;
    align-items: center;
    color: var(--text-white);
  }
  .back-logo .logo-row { display: flex; align-items: center; gap: 10px; }
  .back-logo .logo-dot { background: var(--text-white); }
  .back-logo .logo-name { color: var(--text-white); font-size: 34px; }
  .back-logo .logo-sub { position: static; color: var(--text-white); margin-top: 6px; }
  .website {
    position: absolute;
    left: 0;
    right: 0;
    bottom: 40px;
    text-align: center;
    color: var(--text-white);
    font-size: 13px;
  }
</style>
</head>
<body>
<main class="stage">
  <section class="card card-front" aria-label="Business card front">
    <div class="front-logo">
      <span class="logo-dot"></span>
      <span class="logo-name">HALVERA</span>
    </div>
    <div class="logo-sub">DEVELOPMENTS</div>
    <p class="tagline">Residential Home Building</p>
    <div class="person">
      <p class="person-name">Boris Kalinov</p>
      <p class="person-role">General Manager</p>
    </div>
    <div class="front-rule"></div>
    <div class="front-band"></div>
    <div class="contact">
      <p>Cell # 587.204.XXXX</p>
      <p>Email: bor.kalinov@qwvend.example</p>
    </div>
  </section>

  <section class="card card-back" aria-label="Business card back">
    <div class="back-logo">
      <div class="logo-row">
        <span class="logo-dot"></span>
        <span class="logo-name">HALVERA</span>
      </div>
      <span class="logo-sub">DEVELOPMENTS</span>
    </div>
    <p class="website">www.halvera.example</p>
  </section>
</main>
</body>
</html>
```